Brightvale Kinetics Wordpress Theme

My current wordpress is at: http://brightvalekinetcis.bloghaven.net/

I own the actual domain for mapping.

I'd like the look and feel to be like: http://copperfenlabs.com/

With the front page all black with my logo in the middle (see attached).

The colors should be consistent with my business cards (see attached)

I'd like it to be clean, simple and a little flashy.

Industry/Entity Type

Business

Requirements
Must have
• space for intro video

Plug in ability in wordpress

Calendar of events

Video Press

```html
<!DOCTYPE html>
<html lang="en">
<head>
<meta charset="utf-8">
<title>Brightvale Kinetics</title>
<link rel="stylesheet" href="https://fonts.googleapis.com/css2?family=Michroma&family=Dancing+Script:wght@600&family=Questrial&family=Roboto:wght@400;500&family=Marcellus&display=swap">
<style>
  :root {
    --page-bg: #121416;
    --panel-bg: #0b0c0d;
    --panel-line: #5b5e61;
    --nav-top: #2f74c9;
    --nav-bottom: #1b4f9f;
    --nav-divider: rgba(255,255,255,0.18);
    --text-white: #ffffff;
    --text-body: #e9ecee;
    --text-muted: #8a8d90;
    --accent-blue: #1fa6e3;
    --copy-blue: #2b78b5;
    --signup-orange: #f39a12;
    --arrow-yellow: #f2c21b;
    --chip-bg: #3a3c3f;
    --logo-grey: #bfc3c6;
  }
  * { margin: 0; padding: 0; box-sizing: border-box; }
  html, body { width: 1200px; height: 738px; overflow: hidden; background: #000; }
  .site {
    position: relative; width: 1200px; height: 738px; overflow: hidden;
    background:
      radial-gradient(ellipse 70% 60% at 50% 55%, #24282b 0%, var(--page-bg) 60%, #050606 100%);
    font-family: 'Questrial', sans-serif;
  }
  .topbar { position: absolute; left: 0; top: 0; width: 1200px; height: 54px; background: #050505; }
  .side-strip { position: absolute; top: 54px; height: 76px; width: 1200px; left: 0;
    background: linear-gradient(#0d2f5c, #07162b 80%, transparent); opacity: .7; }
  .nav-band {
    position: absolute; left: 112px; top: 54px; width: 974px; height: 96px;
    background: linear-gradient(var(--nav-top), var(--nav-bottom));
    box-shadow: 0 30px 60px rgba(30,90,190,0.35);
  }
  .nav-band::after { content: ""; position: absolute; left: 0; right: 0; bottom: -40px; height: 40px;
    background: linear-gradient(rgba(30,80,160,0.35), transparent); }
  .main-nav { position: absolute; left: 414px; top: 70px; height: 78px; display: flex; }
  .main-nav a {
    display: flex; align-items: center; padding: 0 14px; height: 78px;
    color: var(--text-white); text-decoration: none; font-family: 'Roboto', sans-serif;
    font-weight: 500; font-size: 12.5px; text-transform: uppercase;
    border-left: 1px solid var(--nav-divider);
  }
  .main-nav a:first-child { border-left: none; }
  .follow-box {
    position: absolute; left: 748px; top: 16px; width: 175px; height: 36px; border-radius: 4px;
    background: var(--chip-bg); display: flex; align-items: center; padding-left: 11px; gap: 8px;
    font-family: 'Roboto', sans-serif; font-size: 12px; font-weight: 500; color: var(--text-white);
  }
  .follow-box .label { margin-right: 6px; }
  .social-square { width: 22px; height: 22px; border-radius: 3px; background: #6d7074; }
  .signup {
    position: absolute; left: 961px; top: 0; width: 76px; height: 25px; background: var(--signup-orange);
    color: var(--text-white); font-family: 'Roboto', sans-serif; font-size: 11px; font-weight: 500;
    display: flex; align-items: center; justify-content: center; gap: 4px;
  }
  .brand-mark { position: absolute; left: 192px; top: 18px; width: 148px; height: 148px;
    border-radius: 50%; background: var(--logo-grey); }
  .brand-name { position: absolute; left: 130px; top: 201px; font-family: 'Questrial', sans-serif;
    font-size: 26px; letter-spacing: 1px; color: var(--logo-grey); text-transform: uppercase; }
  .utility-icons { position: absolute; left: 993px; top: 196px; display: flex; gap: 10px; }
  .panel {
    position: absolute; left: 130px; top: 264px; width: 940px; height: 380px;
    border: 1px solid var(--panel-line); border-radius: 6px;
    background: linear-gradient(#0c0d0e, #101214);
  }
  .headline { position: absolute; left: 161px; top: 306px; font-family: 'Michroma', sans-serif;
    font-size: 29px; line-height: 37px; color: var(--text-white); text-transform: lowercase; font-weight: 400; }
  .tagline { position: absolute; left: 163px; top: 393px; font-family: 'Dancing Script', cursive;
    font-size: 23px; color: var(--accent-blue); }
  .intro { position: absolute; left: 163px; top: 455px; width: 420px; color: var(--text-body);
    font-size: 15.5px; line-height: 23px; }
  .intro p + p { margin-top: 23px; }
  .video-hint { position: absolute; left: 780px; top: 289px; width: 120px; text-align: center;
    font-family: 'Dancing Script', cursive; font-size: 15px; line-height: 19px; color: var(--text-white); }
  .hint-arrow { position: absolute; left: 700px; top: 302px; }
  .video-player { position: absolute; left: 626px; top: 359px; width: 413px; height: 235px;
    border: 4px solid var(--text-white); background: #111; box-shadow: 0 20px 30px rgba(0,0,0,.6); }
  .player-top { position: absolute; left: 0; top: 0; right: 0; height: 25px; background: #1d1e1f;
    display: flex; font-family: 'Roboto', sans-serif; font-size: 11px; font-weight: 500; color: #c7c9cb; }
  .player-top span { padding: 0 8px; display: flex; align-items: center; border-right: 1px solid #444; }
  .player-top .share { width: 74px; }
  .player-top .subs { width: 108px; }
  .player-top .hd { margin-left: auto; border: 1px solid #666; height: 15px; margin: 5px 8px 0 auto; padding: 0 4px; font-size: 10px; }
  .video-still { position: absolute; left: 0; top: 25px; right: 0; bottom: 28px;
    background: radial-gradient(ellipse at 55% 40%, #e4e4e4 0%, #a9a9a9 55%, #5a5a5a 100%); }
  .video-title { position: absolute; left: 14px; top: 38px; background: #0d0d0d; color: #fff;
    font-family: 'Roboto', sans-serif; font-weight: 500; font-size: 16px; padding: 5px 8px; }
  .player-controls { position: absolute; left: 0; right: 0; bottom: 0; height: 28px; background: #1a1b1c;
    display: flex; align-items: center; font-family: 'Roboto', sans-serif; font-size: 11px; color: #c7c9cb; }
  .player-controls .time-bar { flex: 1; height: 9px; border: 1px solid #666; margin: 0 8px; }
  .footer-links { position: absolute; left: 130px; top: 679px; display: flex; font-size: 12.5px; color: var(--text-muted); }
  .footer-links a { color: var(--text-muted); text-decoration: none; }
  .footer-links .sep { margin: 0 8px; }
  .copyright { position: absolute; left: 133px; top: 704px; font-size: 12px; color: var(--copy-blue); }
  .contact-cta { position: absolute; left: 822px; top: 666px; font-family: 'Marcellus', serif; font-size: 42px;
    color: #d8dadc; text-shadow: 0 1px 0 #fff; }
  .contact-icon { position: absolute; left: 1040px; top: 674px; }
</style>
</head>
<body>
<div class="site">
  <div class="topbar"></div>
  <div class="side-strip"></div>
  <div class="nav-band"></div>

  <nav class="main-nav">
    <a href="#">About Company</a>
    <a href="#">Our Services</a>
    <a href="#">Hire Us</a>
    <a href="#">Event Calendar</a>
    <a href="#">Free Resources</a>
    <a href="#">Owner Blog</a>
  </nav>

  <div class="follow-box">
    <span class="label">FOLLOW US</span>
    <span class="social-square" aria-label="Social profile"></span>
    <span class="social-square" aria-label="Social profile"></span>
    <span class="social-square" aria-label="News feed"></span>
  </div>

  <a class="signup" href="#">SIGN UP
    <svg width="10" height="10" viewBox="0 0 10 10"><circle cx="5" cy="5" r="4" fill="none" stroke="#fff" stroke-width="1.2"/><path d="M4 3l2 2-2 2" fill="none" stroke="#fff" stroke-width="1.2"/></svg>
  </a>

  <div class="brand-mark" aria-hidden="true"></div>
  <div class="brand-name">Brightvale Kinetics</div>

  <div class="utility-icons">
    <svg width="16" height="14" viewBox="0 0 16 14" aria-label="Home"><path d="M8 1L1 7h2v6h4V9h2v4h4V7h2z" fill="#c9ccce"/></svg>
    <svg width="16" height="14" viewBox="0 0 16 14" aria-label="Email"><rect x="1" y="3" width="14" height="9" fill="#c9ccce"/><path d="M1 3l7 5 7-5" fill="none" stroke="#222" stroke-width="1"/></svg>
  </div>

  <section class="panel"></section>
  <h1 class="headline">we are a company<br>that empowers futures.</h1>
  <div class="tagline">Eque porro quisquam est qui dolorem!</div>
  <div class="intro">
    <p>Lorem Ipsum is simply dummy text of the printing and typesetting industry. Lorem Ipsum has been the industry's standard dummy text ever since the 1500s.</p>
    <p>When an unknown printer took a galley of type and scrambled it to make a type specimen book.</p>
  </div>

  <div class="video-hint">click here to<br>watch our intro!</div>
  <svg class="hint-arrow" width="82" height="40" viewBox="0 0 82 40">
    <path d="M78 8C55 4 28 10 12 32" fill="none" stroke="var(--arrow-yellow)" stroke-width="2"/>
    <path d="M6 36l2-10 8 6z" fill="var(--arrow-yellow)"/>
  </svg>

  <div class="video-player">
    <div class="player-top">
      <span class="share">Share&nbsp;&nbsp;▾</span>
      <span class="subs">No Subtitles&nbsp;&nbsp;▾</span>
      <span class="hd">HD</span>
    </div>
    <div class="video-still" role="img" aria-label="Intro video still: radio tower against a grey sky with a play button"></div>
    <div class="video-title">ClipHarbor demo</div>
    <div class="player-controls">
      <svg width="36" height="28" viewBox="0 0 36 28"><path d="M13 8l10 6-10 6z" fill="#c7c9cb"/></svg>
      <span>00:00</span>
      <span class="time-bar"></span>
      <span>02:23</span>
      <svg width="52" height="28" viewBox="0 0 52 28"><path d="M6 11h3l4-3v12l-4-3H6z" fill="#c7c9cb"/><path d="M18 14h14" stroke="#c7c9cb"/><path d="M40 9l7 0 0 7M47 19l-7 0 0-7" fill="none" stroke="#c7c9cb" stroke-width="1.4"/></svg>
    </div>
  </div>

  <footer>
    <div class="footer-links">
      <a href="#">About Company</a><span class="sep">|</span>
      <a href="#">Our Services</a><span class="sep">|</span>
      <a href="#">Hire Us</a><span class="sep">|</span>
      <a href="#">Event Calendar</a><span class="sep">|</span>
      <a href="#">Free Resources</a><span class="sep">|</span>
      <a href="#">Owner Blog</a>
    </div>
    <div class="copyright">© 2012 BRIGHTVALE KINETICS, All Rights Reserved.</div>
    <div class="contact-cta">Contact Us</div>
    <svg class="contact-icon" width="30" height="30" viewBox="0 0 30 30" aria-label="Contact">
      <path d="M3 3h14v8h-4V7H7v16h6v-4h4v8H3z" fill="#d8dadc"/>
      <path d="M14 12h7V7l8 8-8 8v-5h-7z" fill="#d8dadc"/>
    </svg>
  </footer>
</div>
</body>
</html>
```